KT Design Business Card

I would like a business card similar to this
https://www.artquorra.com/design/8173920
with my info and a picture of my rifle. You can use something like this
https://www.snaplirra.com/pin/381926405572018843/visual-search/?cropSource=6&h=476&w=268&x=12&y=12
or
https://www.snaplirra.com/pin/219604837751093468/

I have a logo, it is a shepperds staff. I build custom rifles and do Law Enforcement sales. Some where on the card it needs to say something like, "Custom AR's built correctly", "All rifles come with honed uppers and bedded barrels", "All rifles are fully tested and come with a 3 shot card", "Law Enforcement models are available", "Tactical Equipment Consulting", "One stop shop for all tactical equipment"

Business Name: KT Design LLC
Name: Brent Hollis
Phone: (555) 614-2980
Email: brent.ktdesign@mailbriq.com
Address: 3082 Tamblin Ct., Corvell Springs, NC, 29815

Just use the concept of the staff in the attachments the other stuff is not related

```html
<!DOCTYPE html>
<html lang="en">
<head>
<meta charset="utf-8">
<title>KT Design Business Card</title>
<link rel="stylesheet" href="https://fonts.googleapis.com/css2?family=Open+Sans:wght@400;600&display=swap">
<style>
  :root {
    --page: #2a2622;
    --ink: #ffffff;
    --ink-soft: #d9d6d0;
    --card-black: #070707;
    --card-grey: #4a4a48;
    --photo-olive: #6b6552;
    --photo-steel: #8c8b86;
    --photo-dust: #4b4239;
    --photo-deep: #1d1a17;
  }
  * { margin: 0; padding: 0; box-sizing: border-box; }
  html, body { width: 1200px; height: 1023px; overflow: hidden; }
  body {
    background: var(--page);
    font-family: "Open Sans", sans-serif;
    color: var(--ink);
    position: relative;
  }
  .card {
    position: absolute;
    left: 180px;
    width: 840px;
    height: 480px;
    border-radius: 28px;
    overflow: hidden;
  }
  .card--front { top: 21px; background: linear-gradient(160deg, var(--card-black) 0%, var(--card-black) 45%, var(--card-grey) 100%); }
  .card--back { top: 522px; background: var(--photo-deep); }

  .photo { position: absolute; }
  .card--front .photo {
    left: 300px; top: 0; width: 540px; height: 480px;
    background: radial-gradient(ellipse at 45% 50%, var(--photo-steel) 0%, var(--photo-olive) 40%, var(--photo-dust) 75%, #3a342d 100%);
    -webkit-mask-image: linear-gradient(90deg, transparent 0%, #000 25%);
            mask-image: linear-gradient(90deg, transparent 0%, #000 25%);
  }
  .card--back .photo {
    inset: 0;
    background: radial-gradient(ellipse at 70% 40%, #5c5146 0%, var(--photo-dust) 45%, var(--photo-deep) 100%);
  }

  .brand { position: absolute; left: 70px; top: 220px; }
  .brand__name {
    display: flex; align-items: center; gap: 12px;
    font-size: 30px; font-weight: 600; letter-spacing: 1px;
  }
  .brand__mark { width: 14px; height: 14px; border-radius: 50%; background: var(--ink); }
  .brand__model {
    margin-top: 10px; margin-left: 26px;
    font-size: 15px; line-height: 1.35; color: var(--ink-soft); text-transform: uppercase;
  }
  .divider { position: absolute; left: 330px; top: 150px; width: 1px; height: 200px; background: var(--ink); }
  .contact { position: absolute; left: 370px; top: 130px; }
  .contact__name { font-size: 38px; font-weight: 600; letter-spacing: 1px; line-height: 1; }
  .contact__role { font-size: 17px; margin-top: 6px; }
  .contact__address { font-size: 18px; line-height: 1.4; margin-top: 26px; }
  .contact__line { display: flex; align-items: center; gap: 10px; font-size: 18px; margin-top: 10px; }
  .contact__line:first-of-type { margin-top: 22px; }
  .contact__line svg { width: 16px; height: 16px; fill: var(--ink); flex: none; }

  .features {
    position: absolute; left: 60px; top: 110px; list-style: none;
    font-size: 20px; line-height: 1.9;
  }
  .features li::before { content: "— "; color: var(--ink-soft); }
</style>
</head>
<body>
  <section class="card card--front">
    <div class="photo" role="img" aria-label="Photograph of a custom AR-style rifle lying on an olive gear bag"></div>
    <div class="brand">
      <div class="brand__name"><span class="brand__mark"></span>KT DESIGN</div>
      <div class="brand__model">KTD 15<br>Multi Cal<br>S/N: XXXXX</div>
    </div>
    <div class="divider"></div>
    <div class="contact">
      <div class="contact__name">BRENT HOLLIS</div>
      <div class="contact__role">Director</div>
      <div class="contact__address">3082 Tamblin Ct.,<br>Corvell Springs, NC, 29815</div>
      <div class="contact__line">
        <svg viewBox="0 0 24 24"><path d="M6.6 10.8a15 15 0 0 0 6.6 6.6l2.2-2.2a1 1 0 0 1 1-.25 11.4 11.4 0 0 0 3.6.57 1 1 0 0 1 1 1V20a1 1 0 0 1-1 1A17 17 0 0 1 3 4a1 1 0 0 1 1-1h3.5a1 1 0 0 1 1 1c0 1.25.2 2.45.57 3.57a1 1 0 0 1-.25 1z"/></svg>
        555 614-2980
      </div>
      <div class="contact__line">
        <svg viewBox="0 0 24 24"><path d="M2 5h20v14H2zm2 2v.5l8 5 8-5V7zm0 2.8V17h16V9.8l-8 5z"/></svg>
        brent.ktdesign@mailbriq.com
      </div>
    </div>
  </section>

  <section class="card card--back">
    <div class="photo" role="img" aria-label="Dusty photograph of a rifle forend with muzzle device on concrete"></div>
    <ul class="features">
      <li>Custom AR's built correctly</li>
      <li>All rifles are fully tested with a 3 shot card</li>
      <li>Honed uppers and bedded barrels</li>
      <li>Tactical Equipment Consulting</li>
      <li>Law Enforcement models available</li>
    </ul>
  </section>
</body>
</html>
```